Flat bootstrap design for existing site

I'm looking for a modern flat design based around an existing logo. This has to be a custom design (no external templates), and implemented into a bootstrap framework.

The logo is attached as 2 versions - choose whichever you want, that flows better with whatever design you choose.

Added screenshots of the existing site (currently using the default bootstrap layouts). Please make your designs around those pages in the screenshots (i.e. the homepage only has the postal code input and the header). The active page has 3 screenshots, because I wanted to illustrate the other states that would be visible (in the table rows).

This is a moving/junk removal website, just for some context.

Here's some example websites (flat designs) that I like, just to give you an idea of what I'm after.

https://www.plivento.com/
https://hoskadel.com/
https://trumvex.com/
https://bravolinth.com/en/

• It must be a modern/simple flat design, that is built around the existing logo (attached).
• It has to be implemented using bootstrap.

```html
<!DOCTYPE html>
<html lang="en">
<head>
<meta charset="utf-8">
<title>Haulvex — Junk Removal &amp; Moving</title>
<link href="https://fonts.googleapis.com/css2?family=Roboto:wght@300;400;500;700;900&family=Oswald:wght@400;500;600&display=swap" rel="stylesheet">
<style>
:root{
  --sky:#47c3f2;
  --sky-light:#9fdcf7;
  --orange:#f6a11e;
  --orange-dark:#e98f12;
  --ink:#2b2a33;
  --ink-soft:#35333f;
  --paper:#ffffff;
  --mist:#ececec;
  --text:#3a3a3a;
  --muted:#7a7a7a;
}
*{margin:0;padding:0;box-sizing:border-box}
html,body{width:1200px;height:2639px;overflow:hidden}
body{font-family:"Roboto",sans-serif;color:var(--text);background:var(--paper);position:relative}
section,header,footer{position:relative;width:1200px;overflow:hidden}
.abs{position:absolute}
.brand{font-family:"Roboto",sans-serif;font-weight:900;letter-spacing:2px;display:flex;align-items:center;gap:10px}
.btn{display:flex;align-items:center;justify-content:center;border-radius:30px;font-weight:700;text-transform:uppercase}

/* header */
.site-header{height:84px;background:var(--sky);color:var(--paper)}
.site-header .brand{left:252px;top:18px;font-size:42px}
.call{right:348px;top:25px;font-size:11px;white-space:nowrap}
.header-book{left:866px;top:21px;width:84px;height:23px;background:var(--paper);color:var(--sky);font-size:9px}
.main-nav{right:250px;top:54px;display:flex;gap:18px;font-size:11px;font-weight:500}
.main-nav .active{font-weight:700}

/* hero */
.hero{height:479px;background:var(--orange)}
.hero-scene{inset:0;background:linear-gradient(180deg,var(--orange) 0%,var(--orange-dark) 84%,#555 84%,#444 100%)}
.truck-body{left:361px;top:83px;width:581px;height:238px;background:#a7dcf3;border-radius:2px}
.truck-panel{left:372px;top:95px;width:559px;height:214px;background:var(--sky);text-align:center;color:var(--ink)}
.hero h1{font-weight:300;font-size:46px;margin-top:42px;line-height:1}
.hero h2{font-weight:900;font-size:58px;line-height:1.05}
.hero p{font-size:12px;margin-top:6px}

/* welcome */
.welcome{height:387px;background:var(--paper)}
.welcome-title{left:0;width:1200px;top:38px;display:flex;justify-content:center;align-items:center;gap:14px;font-size:38px;font-weight:300;color:#333}
.welcome-title .brand{color:var(--sky);font-size:40px}
.about{left:250px;top:126px;width:345px}
.about h3{font-size:34px;font-weight:300;color:var(--sky)}
.about .lead{font-size:15px;color:var(--muted);margin-top:6px;line-height:1.3}
.about .body{font-size:8.5px;color:var(--muted);margin-top:10px;line-height:1.55}
.about .btn{margin-top:22px;width:144px;height:32px;background:var(--sky);color:var(--paper);font-size:10px}
.about-photo{left:625px;top:130px;width:327px;height:194px;background:linear-gradient(160deg,#d7a26b 0%,#5a6b85 45%,#1e2b44 100%)}

/* how it works */
.how{height:514px;background:var(--sky);color:var(--paper);text-align:center}
.how h2{position:absolute;top:40px;width:100%;font-size:35px;font-weight:900}
.how .intro{position:absolute;top:86px;left:430px;width:340px;font-size:13px;line-height:1.35;color:#e6f6fd}
.step{width:230px;top:170px;display:flex;flex-direction:column;align-items:center}
.step .ring{width:194px;height:194px;border-radius:50%;background:var(--sky-light);display:flex;align-items:center;justify-content:center}
.step .ring-inner{width:158px;height:158px;border-radius:50%;background:var(--sky);display:flex;align-items:center;justify-content:center}
.step .core{width:138px;height:138px;border-radius:50%;background:var(--paper);display:flex;align-items:center;justify-content:center}
.step h4{font-size:13px;font-weight:700;margin-top:18px;text-transform:uppercase}
.step p{font-size:9.5px;margin-top:4px;width:210px;line-height:1.35}

/* news */
.news{height:613px;background:var(--mist);text-align:center}
.news h2{position:absolute;top:38px;width:100%;font-family:"Oswald",sans-serif;font-size:38px;font-weight:600;color:var(--ink)}
.news .intro{position:absolute;top:86px;width:100%;font-family:"Oswald",sans-serif;font-size:15px;letter-spacing:1.4px;color:#444}
.card{top:138px;width:283px;height:388px;background:var(--paper);box-shadow:0 2px 6px rgba(0,0,0,.15);text-align:left}
.card .photo{height:202px}
.card .date{position:absolute;right:0;top:156px;width:66px;text-align:center}
.card .date .day{background:var(--paper);color:var(--sky);font-size:14px;line-height:1.1;padding:6px 0 2px;font-weight:500}
.card .date .day small{display:block;font-size:10px}
.card .date .year{background:var(--sky);color:var(--paper);font-size:12px;padding:3px 0}
.card h5{margin:26px 0 0 14px;font-family:"Oswald",sans-serif;font-size:19px;font-weight:500;color:var(--ink)}
.card hr{margin:12px 14px 0;border:none;border-top:1px solid #ddd}
.card p{margin:12px 14px 0;font-size:9.5px;line-height:1.35;color:#555}
.card .btn{position:absolute;left:10px;top:339px;width:108px;height:30px;background:var(--sky);color:var(--paper);font-size:10px;text-transform:none}

/* newsletter */
.newsletter{height:133px;background:var(--sky);color:var(--paper)}
.newsletter h3{left:250px;top:40px;font-size:28px;font-weight:900}
.newsletter p{left:250px;top:78px;font-size:12px}
.newsletter .btn{left:748px;top:49px;width:202px;height:46px;background:var(--ink);color:var(--paper);font-size:13px}

/* footer */
.site-footer{height:374px;background:linear-gradient(180deg,var(--ink) 0%,var(--ink-soft) 100%);color:var(--paper)}
.site-footer .brand{left:0;width:1200px;justify-content:center;top:48px;font-size:76px;color:var(--sky)}
.foot-nav{top:193px;width:100%;display:flex;justify-content:center;gap:20px;font-size:11px;font-weight:700}
.foot-contact{top:232px;left:394px;width:420px;display:flex;justify-content:space-between;font-size:10px}
.socials{top:282px;width:100%;display:flex;justify-content:center;gap:12px}
.socials span{width:56px;height:56px;border-radius:50%;background:var(--paper)}

/* bottom bar */
.bottom-bar{position:relative;height:55px;background:var(--sky);color:var(--paper);font-size:10px}
.bottom-bar .copy{left:250px;top:24px}
.to-top{left:560px;top:-26px;width:80px;height:70px}
.to-top span{position:absolute;left:0;width:80px;top:26px;text-align:center;font-size:10px;font-weight:700}
</style>
</head>
<body>

<header class="site-header">
  <div class="abs brand">HAULVEX</div>
  <div class="abs call">CALL TO US : 000.000.000</div>
  <div class="abs btn header-book">Book now</div>
  <nav class="abs main-nav">
    <span class="active">HOME</span><span>BOOK</span><span>HOW IT WORK</span><span>BECOME A DRIVER</span><span>SIGN IN</span>
  </nav>
</header>

<section class="hero">
  <div class="abs hero-scene" role="img" aria-label="Flat illustration of a waving mover in a cap beside a blue box truck against an orange city skyline"></div>
  <div class="abs truck-body"></div>
  <div class="abs truck-panel">
    <h1>NEED JUNK REMOVED</h1>
    <h2>BOOK NOW!</h2>
    <p>Lorem Ipsum is simply dummy text of the printing and typesetting industry.</p>
  </div>
</section>

<section class="welcome">
  <div class="abs welcome-title">WELCOME TO <span class="brand">HAULVEX</span></div>
  <div class="abs about">
    <h3>About us</h3>
    <p class="lead">Lorem Ipsum is simply dummy text of the printing and typesetting industry.</p>
    <p class="body">Lorem Ipsum is simply dummy text of the printing and typesetting industry. Lorem Ipsum has been the industry's standard dummy text ever since the 1500s, when an unknown printer took a galley of type and scrambled it to make a type specimen book. It has survived not only five centuries, but also the leap into electronic typesetting, remaining essentially unchanged</p>
    <div class="btn">Read more</div>
  </div>
  <div class="abs about-photo" role="img" aria-label="Photo of a blue semi truck driving at dusk"></div>
</section>

<section class="how">
  <h2>HOW IT WORK</h2>
  <p class="intro">Lorem Ipsum is simply dummy text of the printing and typesetting industry. Lorem Ipsum has been the industry's standard dummy text ever since the 1500s,</p>

  <div class="abs step" style="left:140px">
    <div class="ring"><div class="ring-inner"><div class="core">
      <svg width="70" height="50" viewBox="0 0 70 50" fill="#2b2a33"><rect x="30" y="14" width="24" height="22" rx="3"/><rect x="4" y="28" width="50" height="8"/><circle cx="16" cy="40" r="6"/><circle cx="44" cy="40" r="6"/><path d="M10 6 L30 28" stroke="#2b2a33" stroke-width="3"/><path d="M8 6 v10 a4 4 0 0 0 8 0" stroke="#2b2a33" stroke-width="3" fill="none"/></svg>
    </div></div></div>
    <h4>Home Staging Assistance</h4>
    <p>Lorem Ipsum is simply dummy text of the printing and typesetting industry</p>
  </div>

  <div class="abs step" style="left:365px">
    <div class="ring"><div class="ring-inner"><div class="core">
      <svg width="56" height="72" viewBox="0 0 56 72" role="img" aria-label="Location pin icon"><path d="M28 2 C13 2 3 13 3 27 C3 45 28 70 28 70 C28 70 53 45 53 27 C53 13 43 2 28 2z" fill="#2b2a33"/><circle cx="28" cy="27" r="10" fill="#fff"/></svg>
    </div></div></div>
    <h4>Hourly Labor</h4>
    <p>Lorem Ipsum is simply dummy text of the printing and typesetting industry</p>
  </div>

  <div class="abs step" style="left:600px">
    <div class="ring"><div class="ring-inner"><div class="core">
      <svg width="76" height="50" viewBox="0 0 76 50" fill="#2b2a33"><path d="M14 6 h48 l8 18 v18 h-64 v-18z"/><rect x="18" y="10" width="40" height="12" fill="#fff"/><circle cx="18" cy="32" r="4" fill="#fff"/><circle cx="58" cy="32" r="4" fill="#fff"/><rect x="8" y="40" width="12" height="10"/><rect x="56" y="40" width="12" height="10"/></svg>
    </div></div></div>
    <h4>Storage Solutions</h4>
    <p>Lorem Ipsum is simply dummy text of the printing and typesetting industry</p>
  </div>

  <div class="abs step" style="left:835px">
    <div class="ring"><div class="ring-inner"><div class="core">
      <svg width="80" height="52" viewBox="0 0 80 52" fill="none" stroke="#2b2a33" stroke-width="3"><rect x="18" y="6" width="36" height="32"/><path d="M54 16 h12 l8 10 v12 h-20z"/><circle cx="30" cy="42" r="5"/><circle cx="62" cy="42" r="5"/><path d="M2 14 h12 M6 22 h10 M2 30 h12"/></svg>
    </div></div></div>
    <h4>Long Distance Moving</h4>
    <p>Lorem Ipsum is simply dummy text of the printing and typesetting industry</p>
  </div>
</section>

<section class="news">
  <h2>LATEST NEWS</h2>
  <p class="intro">Lorem Ipsum is simply dummy text of the printing and typesetting industry.</p>

  <article class="abs card" style="left:164px">
    <div class="photo" role="img" aria-label="Photo of a yellow truck on a mountain road" style="background:linear-gradient(160deg,#9fb4c2,#c7a63a 60%,#4f4a3a)"></div>
    <div class="date"><div class="day">15<small>AUG</small></div><div class="year">2017</div></div>
    <h5>MOVE THE WORLD MONDAY</h5><hr>
    <p>Lorem Ipsum is simply dummy text of the printing and typesetting industry. Lorem Ipsum has been the industry's standard dummy text ever since the 1500s</p>
    <div class="btn">Read More</div>
  </article>

  <article class="abs card" style="left:468px">
    <div class="photo" role="img" aria-label="Photo of red trucks parked under a cloudy sky" style="background:linear-gradient(170deg,#6f8fb5,#d88a6a 55%,#7a6f6a)"></div>
    <div class="date"><div class="day">15<small>AUG</small></div><div class="year">2017</div></div>
    <h5>MOVE THE WORLD MONDAY</h5><hr>
    <p>Lorem Ipsum is simply dummy text of the printing and typesetting industry. Lorem Ipsum has been the industry's standard dummy text ever since the 1500s</p>
    <div class="btn">Read More</div>
  </article>

  <article class="abs card" style="left:773px">
    <div class="photo" role="img" aria-label="Photo of a row of white trucks under a blue sky" style="background:linear-gradient(180deg,#5b9ad6,#e8eef3 60%,#9aa3a8)"></div>
    <div class="date"><div class="day">15<small>AUG</small></div><div class="year">2017</div></div>
    <h5>MOVE THE WORLD MONDAY</h5><hr>
    <p>Lorem Ipsum is simply dummy text of the printing and typesetting industry. Lorem Ipsum has been the industry's standard dummy text ever since the 1500s</p>
    <div class="btn">Read More</div>
  </article>
</section>

<section class="newsletter">
  <h3 class="abs">SUBCRIBE FOR NEWSLETTER</h3>
  <p class="abs">Lorem Ipsum is simply dummy text of the printing and typesetting industry</p>
  <div class="abs btn">Subcribe now</div>
</section>

<footer class="site-footer">
  <div class="abs brand">HAULVEX</div>
  <nav class="abs foot-nav"><span>HOME</span><span>BOOK</span><span>HOW IT WORK</span><span>BECOME A DRIVER</span><span>SIGN IN</span></nav>
  <div class="abs foot-contact"><span>PHONE: +000.000.000</span><span>FAX: +000.000.000</span><span>EMAIL:info@haulvex.com</span></div>
  <div class="abs socials" aria-label="Social links"><span></span><span></span><span></span><span></span><span></span><span></span></div>
</footer>

<div class="bottom-bar">
  <div class="abs copy">©Copyright 2017 <b>Haulvex</b> All Rights Reserved</div>
  <div class="abs to-top">
    <svg width="80" height="70" viewBox="0 0 80 70"><path d="M40 0 L80 35 L40 70 L0 35z" fill="#2b2a33"/><path d="M28 22 L40 12 L52 22" fill="#47c3f2"/></svg>
    <span>TOP</span>
  </div>
</div>

</body>
</html>
```